Design for schnapps bottle label "Sol Terrado"

Hi! On a small land lot we are producing our own Italian schnapps "Grappa". For the bottles we would like to modernize our current labes that you find below. The two cats looking at each other should remain, but updated and more modern. I am very much looking forward to your suggestions. Best, Joel

Target Market(s)

Schnapps bottle label

Requirements
Must have
• Cats should resemble the cats that are decorating the house entry (see attached), however, should have a more modern appearance.

Text elements should remain: "Grappa", "Sol Terrado", "Legnoso", "[Vintage Year], "Raccolta No", "Vol %"
Should not have
• Current ornament can be used, replaced or deleted (whatever looks best)

```html
<!DOCTYPE html>
<html lang="it">
<head>
<meta charset="utf-8">
<title>Grappa Legnoso 2015 – Sol Terrado</title>
<link rel="stylesheet" href="https://fonts.googleapis.com/css2?family=Chewy&family=Handlee&family=Open+Sans:wght@400&display=swap">
<style>
  :root {
    --orange: #f59324;
    --orange-light: #f9ad5c;
    --orange-deep: #f48a1c;
    --ink: #3d3a38;
    --cat-grey: #5e5a58;
    --white: #ffffff;
  }
  html, body {
    margin: 0;
    padding: 0;
    overflow: hidden;
    background: #ffffff;
  }
  .label {
    position: relative;
    width: 851px;
    height: 1200px;
    overflow: hidden;
    background: radial-gradient(ellipse at 50% 50%, var(--orange) 55%, var(--orange-light) 100%);
    font-family: "Open Sans", sans-serif;
  }
  .label__frame {
    position: absolute;
    inset: 0;
  }
  .label__title {
    position: absolute;
    top: 120px;
    left: 0;
    width: 100%;
    margin: 0;
    text-align: center;
    font-family: "Chewy", cursive;
    font-weight: 400;
    font-size: 250px;
    line-height: 1;
    letter-spacing: 2px;
    color: var(--ink);
    -webkit-text-stroke: 2px var(--white);
  }
  .label__variety {
    position: absolute;
    top: 435px;
    left: 82px;
    width: 620px;
    margin: 0;
    text-align: center;
    font-family: "Handlee", cursive;
    font-size: 66px;
    line-height: 1;
    color: var(--white);
    white-space: nowrap;
  }
  .label__cat {
    position: absolute;
    top: 595px;
    width: 330px;
    height: 212px;
  }
  .label__cat--left { left: 58px; }
  .label__cat--right { left: 473px; }
  .label__by {
    position: absolute;
    top: 588px;
    left: 400px;
    width: 60px;
    text-align: center;
    font-size: 56px;
    line-height: 1.1;
    color: var(--white);
  }
  .label__producer {
    position: absolute;
    top: 920px;
    left: 0;
    width: 100%;
    margin: 0;
    text-align: center;
    font-family: "Handlee", cursive;
    font-size: 96px;
    font-weight: 400;
    line-height: 1.1;
    color: var(--white);
    text-shadow: 2px 3px 3px rgba(0,0,0,0.25);
  }
  .label__producer .initial { color: var(--ink); }
  .label__footer {
    position: absolute;
    top: 1128px;
    left: 34px;
    right: 34px;
    display: flex;
    justify-content: space-between;
    font-size: 32px;
    line-height: 1.2;
    color: var(--ink);
  }
</style>
</head>
<body>
<main class="label">
  <svg class="label__frame" width="851" height="1200" viewBox="0 0 851 1200" aria-hidden="true">
    <path d="M40 200 C260 110 590 110 811 200 C860 320 800 420 700 560 C640 660 760 760 820 900 C850 990 830 1050 800 1080 C560 1010 290 1010 50 1080 C10 1000 20 950 80 840 C160 700 200 640 130 520 C60 400 20 300 40 200 Z"
          fill="var(--orange-deep)" stroke="#fde0bf" stroke-width="2.5"/>
  </svg>

  <h1 class="label__title">Grappa</h1>
  <p class="label__variety">“legnoso” 2015</p>

  <svg class="label__cat label__cat--left" viewBox="0 0 330 212" role="img" aria-label="Illustration: grey striped cat standing, looking right">
    <rect width="330" height="212" rx="30" fill="var(--cat-grey)" opacity="0.85"/>
  </svg>
  <span class="label__by">di</span>
  <svg class="label__cat label__cat--right" viewBox="0 0 330 212" role="img" aria-label="Illustration: grey striped cat standing, looking left">
    <rect width="330" height="212" rx="30" fill="var(--cat-grey)" opacity="0.85"/>
  </svg>

  <h2 class="label__producer"><span class="initial">Sol</span> <span class="initial">T</span>errado</h2>

  <footer class="label__footer">
    <span class="label__batch">Raccolta No. 01</span>
    <span class="label__abv">41.0 Vol %</span>
  </footer>
</main>
</body>
</html>
```